BrivoMatex. Lantern for the Steady Growth. Business card

Professional business card for BrivoMatex (Lantern for the Steady Growth)
My rationale: Strategy-> Execution-> Results-> Value that lead to the BrivoMatex name: We put the Lantern for the Steady Growth.
We deliver value to our customers helping them at defining a good strategy (cyan arrow). 90% of well formulated strategies fail due to poor execution so we also consider strategical execution very important (green arrow). Due to the execution we obtain the results (blue arrow). Finally, the results provide feedback to redefine strategy, and the new strategy has to be executed and new results obtained providing new feedback and on and on. It's like a wheel that finally, must create corporate value: value for shareholders, staholders, employees, providers...-

Target Market(s)

CEOs and steering comitees , invewrnent funds

Industry/Entity Type

Business Consultant

Contact Information for Business Card

Tommaso Ferlini
CEO & Founder
tommaso.ferlini@brivomatex.example
Mobile: +34 611.205.938
www.brivomatex.example

Colors

Designer to choose colors to be used in the design.

Requirements
Nice to have
• Nice to hace the words: Strategy, execution, results
• Nice to vave the claim: Lantern for the Steady Growth
• The three colors should be shown:
• cyan for STRATEGY
• green for EXECUTION
• blue for RESULTS
Should not have
• Complete black background

```html
<!DOCTYPE html>
<html lang="en">
<head>
<meta charset="utf-8">
<title>BrivoMatex — Business Card</title>
<link rel="stylesheet" href="https://fonts.googleapis.com/css2?family=Nunito:wght@300;400;700;800&display=swap">
<style>
  :root {
    --navy: #223785;
    --green: #8dbe36;
    --cyan: #27a2d6;
    --paper: #f1f1f1;
    --backdrop: #e4e4e4;
  }
  * { margin: 0; padding: 0; box-sizing: border-box; }
  html, body {
    width: 1200px;
    height: 1200px;
    overflow: hidden;
    background: var(--backdrop);
    font-family: "Nunito", sans-serif;
  }
  .sheet { position: relative; width: 1200px; height: 1200px; }
  .card {
    position: absolute;
    left: 227px;
    width: 746px;
    height: 425px;
    border-radius: 43px;
    overflow: hidden;
  }
  .card--front { top: 135px; background: var(--paper); }
  .card--back { top: 640px; background: var(--navy); }
  .card svg { position: absolute; inset: 0; display: block; }

  .wordmark {
    position: absolute;
    font-weight: 800;
    letter-spacing: -1px;
    line-height: 1;
  }
  .card--front .wordmark { left: 36px; top: 156px; font-size: 58px; color: var(--navy); }
  .card--back .wordmark {
    left: 0; right: 0; top: 200px; text-align: center;
    font-size: 70px; color: var(--paper);
  }
  .tagline {
    position: absolute; left: 0; right: 0; top: 276px;
    text-align: center; font-weight: 400; font-size: 21px;
    color: var(--paper); letter-spacing: 0.3px;
  }

  .holder { position: absolute; left: 36px; top: 344px; color: var(--paper); }
  .holder__name { font-size: 23px; font-weight: 400; letter-spacing: 0.6px; line-height: 1.2; }
  .holder__role { font-size: 16px; font-weight: 400; letter-spacing: 0.4px; margin-top: 2px; }

  .contacts {
    position: absolute; right: 34px; top: 321px;
    list-style: none; color: var(--paper);
  }
  .contacts li {
    display: flex; align-items: center; justify-content: flex-end;
    gap: 12px; height: 24px;
    font-size: 16px; font-weight: 400; letter-spacing: 0.4px;
  }
  .contacts svg { position: static; width: 18px; height: 18px; }

  .steps {
    position: absolute; left: 0; right: 0; top: 347px; height: 42px;
    font-size: 23px; font-weight: 700; letter-spacing: 0.5px;
  }
  .steps span { position: absolute; transform: translateX(-50%); line-height: 42px; }
  .step--strategy { left: 122px; color: var(--cyan); }
  .step--execution { left: 363px; color: var(--green); }
  .step--results { left: 615px; color: var(--navy); }
</style>
</head>
<body>
<main class="sheet">

  <section class="card card--front" aria-label="Business card front">
    <svg viewBox="0 0 746 425" width="746" height="425" aria-hidden="true">
      <rect x="0" y="288" width="746" height="5" fill="var(--green)"/>
      <rect x="0" y="300" width="746" height="125" fill="var(--navy)"/>
    </svg>

    <div class="wordmark">BrivoMatex</div>

    <div class="holder">
      <p class="holder__name">Tommaso Ferlini</p>
      <p class="holder__role">CEO &amp; Founder</p>
    </div>

    <ul class="contacts">
      <li>+34 611.205.938
        <svg viewBox="0 0 18 18" aria-hidden="true"><circle cx="9" cy="9" r="9" fill="var(--paper)"/><path d="M4.5,8 Q9,4 13.5,8 L12.5,9.5 L11,8.5 L7,8.5 L5.5,9.5 Z M6,10 H12 V13 H6 Z" fill="var(--navy)"/></svg>
      </li>
      <li>tommaso.ferlini@brivomatex.example
        <svg viewBox="0 0 18 18" aria-hidden="true"><circle cx="9" cy="9" r="9" fill="var(--paper)"/><rect x="4.5" y="5.5" width="9" height="7" fill="none" stroke="var(--navy)" stroke-width="1.3"/><path d="M4.5,5.5 L9,9.5 L13.5,5.5" fill="none" stroke="var(--navy)" stroke-width="1.3"/></svg>
      </li>
      <li>www.brivomatex.example
        <svg viewBox="0 0 18 18" aria-hidden="true"><circle cx="9" cy="9" r="9" fill="var(--paper)"/><circle cx="9" cy="9" r="5" fill="none" stroke="var(--navy)" stroke-width="1.3"/><path d="M4,9 H14 M9,4 V14" stroke="var(--navy)" stroke-width="1"/></svg>
      </li>
    </ul>
  </section>

  <section class="card card--back" aria-label="Business card back">
    <svg viewBox="0 0 746 425" width="746" height="425" aria-hidden="true">
      <rect x="0" y="346" width="746" height="43" fill="var(--paper)"/>
      <path d="M225,346 L249,367.5 L225,389" fill="none" stroke="var(--navy)" stroke-width="2.5"/>
      <path d="M478,346 L502,367.5 L478,389" fill="none" stroke="var(--navy)" stroke-width="2.5"/>
    </svg>

    <div class="wordmark">BrivoMatex</div>
    <p class="tagline">Lantern for the Steady Growth</p>

    <div class="steps">
      <span class="step--strategy">STRATEGY</span>
      <span class="step--execution">EXECUTION</span>
      <span class="step--results">RESULTS</span>
    </div>
  </section>

</main>
</body>
</html>
```